Mipo! Label for Sauce and Brine Comapny

Hello! I would love a label for my jars of sauce and bags of brine mix. Some of the requirements will be a QR code that sends people to my website for recipe ideas. There has to be a place to put a batch number, and space to write in names of sauces and brines as they are changing with the seasons. I have an emblem but I don't love it so I am open to changing it to better fit the label. The sauces are made with local, seasonal ingredients in small batches, the brines reflect current flavor trends based to time of year as well. The label should also include Made in Saint Louis, and a place for me to customize the ingredients list. The emblem is posted below, again it is not required for the label, this label was made when I had a different concept in mind. The name of my company is called Mipo! I would not like a blue design. Again the design should look fresh, local, and changing with the seasons while highlighting small batch and chef made flavors.

Target Market(s)

20-50 at home cooks/ foodies

Industry/Entity Type

food/ beverage

Font styles to use
Sans Serif
Decorative
Script

Colors
00AB8E
00BBA5
67D7C9
C6EFE9
E9F9F6
FFF300
FFF600
FEFA6F
FFFEC7
FFFEE8
F0912C
F2A743
F7CA91
FBE8D2
FDF5EE

Requirements
Must have
• QR CODE to website, area for batch numbers, area for changing listed ingredients, made in saint louis,
Nice to have
• I would love to have a label that maybe has a window somewhere to see the sauce, but that is not required
Should not have
• no blue please

```html
<!DOCTYPE html>
<html lang="en">
<head>
<meta charset="utf-8">
<title>Mipo! Butternut Hoisin Lid Label</title>
<link rel="stylesheet" href="https://fonts.googleapis.com/css2?family=Open+Sans:wght@600;800&display=swap">
<style>
  :root {
    --page: #ffffff;
    --lid: #fbfbfb;
    --lid-edge: #e4e4e4;
    --halo: #fef36a;
    --orange-top: #f2bd1e;
    --orange-bottom: #ec8a1c;
    --rim-orange: #f0912c;
    --title-red: #d8472b;
    --box: #ffffff;
    --leaf: #4e9a2b;
    --nut: #c98a55;
  }
  html, body {
    margin: 0;
    padding: 0;
    width: 1200px;
    height: 1200px;
    overflow: hidden;
    background: var(--page);
  }
  .lid-label {
    display: block;
    width: 1200px;
    height: 1200px;
  }
  .brand-name {
    font-family: "Open Sans", sans-serif;
    font-weight: 800;
    font-size: 150px;
    fill: var(--rim-orange);
  }
  .flavor-title {
    font-family: "Open Sans", sans-serif;
    font-weight: 600;
    font-size: 112px;
    fill: var(--title-red);
  }
  .ingredient-list {
    font-family: "Open Sans", sans-serif;
    font-weight: 600;
    font-size: 50px;
    fill: var(--title-red);
    stroke: var(--halo);
    stroke-width: 9px;
    paint-order: stroke;
    stroke-linejoin: round;
  }
</style>
</head>
<body>
<svg class="lid-label" viewBox="0 0 1200 1200" xmlns="http://www.w3.org/2000/svg">
  <defs>
    <linearGradient id="flavor-disk-fill" x1="0" y1="0" x2="0" y2="1">
      <stop offset="0" stop-color="var(--orange-top)"/>
      <stop offset="1" stop-color="var(--orange-bottom)"/>
    </linearGradient>
    <radialGradient id="ingredient-art-fill" cx="0.5" cy="0.5" r="0.6">
      <stop offset="0" stop-color="var(--nut)"/>
      <stop offset="0.55" stop-color="#7fa83a"/>
      <stop offset="1" stop-color="var(--leaf)"/>
    </radialGradient>
    <clipPath id="flavor-disk-clip">
      <circle cx="600" cy="650" r="400"/>
    </clipPath>
    <path id="ingredient-arc" d="M139,560 A470,470 0 1 0 1061,560"/>
  </defs>

  <circle class="lid-surface" cx="600" cy="600" r="585" fill="var(--lid)" stroke="var(--lid-edge)" stroke-width="6"/>

  <path class="rim-arc" d="M178,770 A445,445 0 0 1 300,320" fill="none" stroke="var(--halo)" stroke-width="22" stroke-linecap="round"/>
  <path class="rim-arc" d="M178,770 A445,445 0 0 1 300,320" fill="none" stroke="var(--rim-orange)" stroke-width="7" stroke-linecap="round"/>
  <path class="rim-arc" d="M900,320 A445,445 0 0 1 1022,770" fill="none" stroke="var(--halo)" stroke-width="22" stroke-linecap="round"/>
  <path class="rim-arc" d="M900,320 A445,445 0 0 1 1022,770" fill="none" stroke="var(--rim-orange)" stroke-width="7" stroke-linecap="round"/>

  <circle class="flavor-halo" cx="600" cy="650" r="418" fill="var(--halo)"/>
  <circle class="flavor-disk" cx="600" cy="650" r="400" fill="url(#flavor-disk-fill)"/>

  <path class="brand-banner" d="M262,300 C400,250 480,300 600,270 C720,240 800,200 910,215 C905,280 905,340 910,400 C800,395 720,450 580,445 C450,440 350,420 270,450 C262,400 258,350 262,300 Z" fill="var(--halo)"/>
  <path class="brand-banner-line" d="M275,438 C370,410 460,428 580,434 C720,440 790,392 898,392" fill="none" stroke="var(--title-red)" stroke-width="6" stroke-linecap="round"/>
  <text class="brand-name" x="585" y="385" text-anchor="middle">Mipo!</text>

  <text class="flavor-title" x="600" y="560" text-anchor="middle">Butternut</text>
  <text class="flavor-title" x="600" y="676" text-anchor="middle">Hoisin</text>

  <rect class="qr-space" x="268" y="715" width="135" height="148" rx="16" fill="var(--box)"/>
  <rect class="batch-space" x="714" y="712" width="238" height="74" rx="14" fill="var(--box)"/>

  <circle class="origin-badge" cx="600" cy="790" r="58" fill="none" stroke="#ffffff" stroke-width="5"/>

  <g clip-path="url(#flavor-disk-clip)">
    <ellipse class="ingredient-art" cx="660" cy="975" rx="300" ry="120" fill="url(#ingredient-art-fill)" role="img" aria-label="Illustration of green leaves, peanuts in the shell and a dollop of peanut butter"/>
  </g>

  <text class="ingredient-list">
    <textPath href="#ingredient-arc" startOffset="50%" text-anchor="middle">Butternut Squash . Peanut Butter . Ginger . Garlic . Spices</textPath>
  </text>
</svg>
</body>
</html>
```